Yoga/movement guide/teacher for adult yoga practice and kid yoga

What is the positioning or mission statement of your company? to guide individuals in a yoga-based safe and sustainable movement practice applicable to all ages and body types. Currently my focus is working with children in daycare and school settings, but my goal is to expand into private yoga practice for adults, and potentially as part of rented space in studios. I hope to find a way to work with children AND adults (so would love for logo to be appealing to both), but current focus is with children based on need and demand in the community. yoga for children also compliments my backround as a pediatrician/neonatologist, and I greatly miss interacting with children. I also want to emphasize a yoga/movement practice that is focused more on what one feels internally through movement. NOT what one looks like asthetically. I believe in removing all mirrors from yoga/movement practice. It should be an experience of movement/poses/yoga through appropriate cueing and education. It is not about the details of how far the knee should bend, or how high the leg should be. Focusing on foudation first, core, then core engagement and ultimately expression of poses/movements. A focus on strength, stability and mobility, not just flexibility, which is the common perception/association with yoga. I also want individuals to learn to be an advocate of their own health. Through guidance, I hope for individuals to connect with their body so they know themselves so well to be able to advocate for themselves in the modern healthcare world. This internal experience and connection is so essential in a world where modern medicine has become a business and it is all about making a dollar. the connection with patients is lost, and individuals need to learn to empower themselves and through their new found voice to be able to articulate what is wrong.<br/>Does your company have a tagline or slogan that should be included with the logo? "Move With Inner Light"<br/>What do you hope your company can be known for? Accessible yoga for a sustained practice. A guided movement practice where one gains information and knowledge of oneself through a mind/body connection. For one feel good physically with a new awaraness of their internal radiance that exists in all beings. Physical rejuvenation egnites a light and increases energy to flow through the physical body, which ultimately tranlates into works of kindness for others and out in the world. <br/>What color palettes might you prefer? why? love the colors currently chosen<br/>Where will the logo be primarily used? initially business cards, but hopefully future websites, t-shirts, and potentially local magazine adds. Also starting with a small couple of banners for community events in the area. I currently practice as a nomad out of my car :)<br/>Are there any elements you would prefer to see in the logo? Movement. A modern depiction of a human body/figure practicing movement. Hoping to avoid a stereotypical yoga pose per say, just because I want to people to think of it more of a movement practice with yoga roots. Modern yoga. There are elements of breathing and connecting with oneself through the flow of breath and movement, but I do not focus on the meditative/cerebral aspect of the yoga practice. What I teach is almost reaching a meditative state through movement. I personally don't practice, nor resonate with just seated meditation. just not my thing :)<br/>In your opinion, what defines a well-designed logo? curiosity. enough info for individuals to think they know what it means, but want to know more. invokes curiosity, but not too abstract. Reproducible. not too complicated. I want also to invoke a community feel, so a design that appeals to all people within a community. <br/>What is your preference in reference to icons, typography, spokespeople (characters), etc.? modern design. I love the idea of a logo for my purposes, to invoke a sense of movement from within. So not too static. <br/>What words or icons must be included in the logo? movement with yoga roots. <br/>What logos do you like and why? A representation, but not exact. I think some ambiguity is intriguing for others, and also memorable. I want it to be an artistic representation of movement/yoga<br/>What logos do you dislike and why? too busy, too loud. <br/>In your opinion, what is the primary purpose for a logo? association<br/>Who is the primary target audience? (who is most likely to use your services/product?) Children and their parents, but ultimately to expand into teaching adults. I even have aspirations of prenatal and post-natal yoga. Potentially incorporating infants. <br/>Who currently uses your product the most? n/a (working in schools/daycare currently. It is currently all volunteer)<br/>Are you pleased with the range of people your company serves? n/a<br/>Are you looking to expand, modify, or completely change your target audience? or will it remain the same? yes! expand into an adult audience. <br/>How do you plan to focus on your target audience? currently by working through schools and daycares. hopefully ultimately through after school care programs and then offering kid yoga in an existing yoga studio (working on this with Quillbrook in Ridgeland, currently)<br/>What are your main forms of advertising? word of mouth, schools, daycares. Happy kids talking to their parents about the yoga class they took and happy teachers :)<br/>How do most customers find out about your company?<br/>Which gender are you targeting? All genders! However, with kid yoga, often the maternal individual in the child's life is more involved with decision making as far as extracurricular activities

Target Market(s)

individuals and families interested in wellness and feeling great

Contact Information for Business Card

Dana Whitford
Yoga Instructor
RYT-200, RCYT

certified yoga teacher for adults and children

Colors

Requirements
Must have
• "Move With Inner Light"
Nice to have
• logo with same colors

```html
<!DOCTYPE html>
<html lang="en">
<head>
<meta charset="utf-8">
<title>Lumen Grove Studio – Business Card</title>
<link rel="stylesheet" href="https://fonts.googleapis.com/css2?family=Montserrat:wght@300;400;500;800&display=swap">
<style>
  :root {
    --backdrop: #e8e4de;
    --card: #f7f7f7;
    --sun: #ecd43a;
    --sea: #62c4cc;
    --sky: #1fa7df;
    --ink: #333333;
    --stone: #6d6e70;
    --white: #ffffff;
  }
  * { margin: 0; padding: 0; box-sizing: border-box; }
  html, body {
    width: 900px; height: 1200px; overflow: hidden;
    background: var(--backdrop);
    font-family: "Montserrat", Arial, sans-serif;
  }
  .card {
    position: absolute; left: 75px; width: 768px; height: 438px;
    background: var(--card); border-radius: 20px; overflow: hidden;
    box-shadow: 0 6px 18px rgba(0,0,0,.18);
  }
  .card--front { top: 133px; }
  .card--back  { top: 628px; }
  .card__waves { position: absolute; inset: 0; }

  .brand { position: absolute; display: flex; flex-direction: column; }
  .brand__name { color: var(--stone); font-weight: 400; line-height: 1.08; }
  .brand__tagline {
    color: var(--sea); font-weight: 400; text-transform: uppercase;
    letter-spacing: 2px;
  }
  .card--front .brand { left: 56px; top: 120px; }
  .card--front .brand__name { font-size: 38px; }
  .card--front .brand__tagline { font-size: 11px; margin-top: 16px; }

  .card--back .brand { left: 0; right: 0; top: 150px; align-items: center; text-align: center; }
  .card--back .brand__name { font-size: 54px; }
  .card--back .brand__tagline { font-size: 14px; margin-top: 22px; }

  .person { position: absolute; right: 41px; top: 80px; text-align: right; }
  .person__name { color: var(--sky); font-weight: 800; font-size: 28px; letter-spacing: .5px; }
  .person__role { color: var(--ink); font-size: 19px; }

  .contact { position: absolute; right: 40px; top: 305px; list-style: none; }
  .contact__item {
    display: flex; justify-content: flex-end; align-items: center;
    color: var(--ink); font-size: 19px; height: 32px;
  }
  .contact__icon {
    width: 24px; height: 24px; margin-left: 10px;
    background: var(--white); border-radius: 50%;
    display: flex; align-items: center; justify-content: center;
  }
  .contact__icon svg { width: 14px; height: 14px; fill: var(--sky); }
</style>
</head>
<body>

<section class="card card--front">
  <svg class="card__waves" viewBox="0 0 768 438" aria-hidden="true">
    <path d="M0,280 C110,345 260,335 395,268 L300,438 L0,438 Z" fill="var(--sun)"/>
    <path d="M0,312 C110,372 260,360 388,282 L292,438 L0,438 Z" fill="var(--white)"/>
    <path d="M0,318 C110,378 262,366 390,286 L294,438 L0,438 Z" fill="var(--sea)"/>
    <path d="M292,442 C360,300 500,205 780,225 L780,442 Z" fill="var(--sun)" stroke="var(--white)" stroke-width="5"/>
  </svg>

  <div class="brand">
    <span class="brand__name">Lumen Grove<br>Studio</span>
    <span class="brand__tagline">Move With Inner Light</span>
  </div>

  <div class="person">
    <h1 class="person__name">DANA WHITFORD</h1>
    <p class="person__role">Director</p>
  </div>

  <ul class="contact">
    <li class="contact__item">01 98 76 5432
      <span class="contact__icon"><svg viewBox="0 0 24 24"><path d="M6.6 10.8a15.1 15.1 0 0 0 6.6 6.6l2.2-2.2c.3-.3.7-.4 1-.2 1.1.4 2.3.6 3.6.6.6 0 1 .4 1 1V20c0 .6-.4 1-1 1A17 17 0 0 1 3 4c0-.6.4-1 1-1h3.5c.6 0 1 .4 1 1 0 1.3.2 2.5.6 3.6.1.3 0 .7-.2 1z"/></svg></span>
    </li>
    <li class="contact__item">hello@lumengrove.com
      <span class="contact__icon"><svg viewBox="0 0 24 24"><path d="M3 5h18v2l-9 6-9-6z M3 9l9 6 9-6v10H3z"/></svg></span>
    </li>
    <li class="contact__item">www.lumengrove.com
      <span class="contact__icon"><svg viewBox="0 0 24 24"><path d="M12 2a7 7 0 0 0-7 7c0 5 7 13 7 13s7-8 7-13a7 7 0 0 0-7-7zm0 9.5A2.5 2.5 0 1 1 12 6.5a2.5 2.5 0 0 1 0 5z"/></svg></span>
    </li>
  </ul>
</section>

<section class="card card--back">
  <div class="brand">
    <span class="brand__name">Lumen Grove<br>Studio</span>
    <span class="brand__tagline">Move With Inner Light</span>
  </div>
</section>

</body>
</html>
```